2367 Halvorsen Avenue Medical Centre

We are looking for a design for new medical clinic.
We are accepting new patients at this new medical centre grand opening. Walk-ins are welcome.
Our cardiac and vascular surgical specialists are department heads at St Alder's Hospital, a leading teaching hospital in Toronto. These specialists will see cardiovascular consults are well as pre-surgical and post-surgical consultations and follow-ups.
Our lab is affiliated with several nuclear medicine clinics in the GTA.
Our Services Includes:
Family Practice
Cardiology Diagnostics
Cardiac & Vascular Surgical Consultation
Ultrasound & Vascular Testing
Open 6 days a week.
Ample Free Parking
Friendly Staffs

Target Market(s)

New Patients. Families of any age. Ethnic groups including Asians & Africans.

Industry/Entity Type

Medical

Font styles to use
Serif
Sans Serif
Decorative
Script
Other font styles liked:
• Arial calibri, verdana

Requirements
Must have
• Address:
• 2367 Halvorsen Avenue East
• Unit 225
• Scarborough, Ontario
• K7T 2P4
• Tel: (416) 555-0148
Nice to have
• Caring and inviting environment.
• Simple but classy.
• Standout colors.
Should not have
• Busy images. Aside from this, any ideas are welcome.

```html
<!DOCTYPE html>
<html lang="en">
<head>
<meta charset="utf-8">
<title>2367 Halvorsen Avenue Medical Centre</title>
<link rel="stylesheet" href="https://fonts.googleapis.com/css2?family=Quicksand:wght@300;400;500;600;700&display=swap">
<style>
  :root {
    --teal: #5aa3b9;
    --sky: #86c6d8;
    --sky-dark: #5c9fb4;
    --lime: #a5cb4f;
    --lime-text: #9bc541;
    --ink: #2e2e2e;
    --grey-bg: #d6d6d6;
    --paper: #fbfbfb;
    --white: #ffffff;
  }
  * { margin: 0; padding: 0; box-sizing: border-box; }
  html, body { width: 1200px; height: 1052px; overflow: hidden; }
  body {
    background: var(--grey-bg);
    font-family: "Quicksand", sans-serif;
    color: var(--ink);
    position: relative;
  }
  .poster {
    position: absolute;
    left: 241px; top: 21px;
    width: 815px; height: 1147px;
    transform: scale(0.88);
    transform-origin: 0 0;
    background: linear-gradient(100deg, var(--paper) 0%, #f3f3f3 60%, #e9e9e9 100%);
    overflow: hidden;
    box-shadow: 0 8px 24px rgba(0,0,0,.18);
  }
  .poster * { position: absolute; }
  .hero-photo {
    left: 420px; top: 40px; width: 395px; height: 680px;
    background: radial-gradient(ellipse at 35% 25%, #e8dede 0%, #d9d9d9 35%, #cfcfcf 55%, rgba(240,240,240,0) 80%);
  }
  .shapes { left: 0; top: 0; width: 815px; height: 1147px; }
  .t { white-space: nowrap; line-height: 1; }
  .num { font-weight: 700; color: var(--teal); }
  .street { font-weight: 300; letter-spacing: 1px; }
  .centre { font-weight: 700; color: var(--teal); letter-spacing: 1px; }
  .intro { font-weight: 400; letter-spacing: .5px; }
  .rule { left: 250px; top: 277px; width: 190px; height: 2px;
    background: linear-gradient(90deg, rgba(230,150,150,0), rgba(230,150,150,.7), rgba(230,150,150,0)); }
  .services-title { color: var(--lime-text); font-weight: 700; font-size: 38px; left: 30px; top: 442px; }
  .services-sub { color: var(--lime-text); font-weight: 300; font-size: 30px; left: 30px; top: 481px; }
  .service { width: 170px; text-align: center; }
  .service-photo {
    position: absolute; left: 28px; top: -2px; width: 114px; height: 114px; border-radius: 50%;
    background: radial-gradient(circle at 40% 40%, #e9eef3, #a9bfd3);
  }
  .service-ring { position: absolute; left: 14px; top: -16px; width: 142px; height: 142px; }
  .service-label { position: static; display: block; padding-top: 132px; font-weight: 700; font-size: 16px; line-height: 20px; color: var(--ink); }
  .open { color: var(--teal); font-weight: 700; font-size: 40px; letter-spacing: 2px; }
  .open .six { position: static; color: var(--lime-text); }
  .book { left: 580px; top: 859px; color: var(--white); font-weight: 700; font-size: 15px; line-height: 20px; letter-spacing: 1px; }
  .phone { left: 490px; top: 928px; color: var(--white); font-weight: 700; font-size: 38px; letter-spacing: 1px; }
  .walkin { left: 468px; top: 975px; font-weight: 700; font-size: 17px; letter-spacing: 1.5px; color: var(--ink); }
  .foot-name { color: var(--white); }
  .address { left: 470px; top: 1037px; color: var(--white); font-size: 14px; line-height: 17.5px; font-weight: 400; }
  .address strong { position: static; display: block; font-weight: 700; font-size: 13px; }
</style>
</head>
<body>
<main class="poster">
  <div class="hero-photo" role="img" aria-label="Photo of a hand holding a small red heart"></div>

  <svg class="shapes" viewBox="0 0 815 1147" aria-hidden="true">
    <path d="M505,905 C620,870 760,800 815,712 L815,905 Z" fill="var(--lime)"/>
    <path d="M0,952 C160,935 320,955 418,1020 L418,1147 L0,1147 Z" fill="var(--white)"/>
    <path d="M0,964 C160,948 318,966 410,1028 L400,1147 L0,1147 Z" fill="var(--sky)"/>
    <path d="M505,905 L815,905 L815,1020 L415,1020 Z" fill="var(--sky)"/>
    <path d="M415,1020 L815,1020 L815,1147 L400,1147 Z" fill="var(--lime)"/>
    <path d="M415,1020 L432,1020 L424,1034 Z" fill="var(--sky-dark)"/>
  </svg>

  <div class="t num" style="left:32px;top:32px;font-size:56px;">2367</div>
  <div class="t street" style="left:32px;top:93px;font-size:39px;">HALVORSEN AVENUE</div>
  <div class="t centre" style="left:32px;top:139px;font-size:32px;">MEDICAL CENTRE</div>
  <div class="t intro" style="left:34px;top:188px;font-size:25px;">NEW MEDICAL CLINIC</div>
  <div class="t intro" style="left:34px;top:215px;font-size:21px;">Pre-surgical and post-surgical</div>
  <div class="t intro" style="left:34px;top:241px;font-size:21px;">Consultations and follow-ups</div>
  <div class="rule"></div>
  <div class="t intro" style="left:34px;top:320px;font-size:24px;line-height:30px;white-space:normal;width:420px;">Our lab is affiliated with several Nuclear medicine clinics in the GTA</div>

  <div class="t services-title">SERVICES</div>
  <div class="t services-sub">INCLUDES</div>

  <div class="service" style="left:20px;top:553px;">
    <div class="service-photo" role="img" aria-label="Doctor examining a child held by a parent"></div>
    <svg class="service-ring" viewBox="0 0 142 142" aria-hidden="true"><circle cx="71" cy="71" r="66" fill="none" stroke="var(--sky)" stroke-width="8" stroke-linecap="round" stroke-dasharray="0 12.4"/></svg>
    <span class="service-label">Family Practice</span>
  </div>
  <div class="service" style="left:187px;top:553px;">
    <div class="service-photo" role="img" aria-label="Red heart resting on an ECG chart with a stethoscope"></div>
    <svg class="service-ring" viewBox="0 0 142 142" aria-hidden="true"><circle cx="71" cy="71" r="66" fill="none" stroke="var(--sky)" stroke-width="8" stroke-linecap="round" stroke-dasharray="0 12.4"/></svg>
    <span class="service-label">Cardiology<br>Diagnostics</span>
  </div>
  <div class="service" style="left:20px;top:750px;">
    <div class="service-photo" role="img" aria-label="Surgical team in an operating room"></div>
    <svg class="service-ring" viewBox="0 0 142 142" aria-hidden="true"><circle cx="71" cy="71" r="66" fill="none" stroke="var(--sky)" stroke-width="8" stroke-linecap="round" stroke-dasharray="0 12.4"/></svg>
    <span class="service-label">Cardiac &amp; Vascular<br>Surgical Consultation</span>
  </div>
  <div class="service" style="left:187px;top:750px;">
    <div class="service-photo" role="img" aria-label="Ultrasound machine control panel"></div>
    <svg class="service-ring" viewBox="0 0 142 142" aria-hidden="true"><circle cx="71" cy="71" r="66" fill="none" stroke="var(--sky)" stroke-width="8" stroke-linecap="round" stroke-dasharray="0 12.4"/></svg>
    <span class="service-label">Ultrasound &amp;<br>Vascular</span>
  </div>

  <div class="t open" style="left:397px;top:665px;">OPEN <span class="six">6</span> DAYS</div>
  <div class="t open" style="left:397px;top:714px;">A WEEK</div>

  <div class="t book">TO BOOK APPOINTMENT,<br>PLEASE CALL</div>
  <div class="t phone">(416) 555-0148</div>
  <div class="t walkin">ACCEPTING WALK-IN PATIENTS</div>

  <div class="t num foot-name" style="left:36px;top:1016px;font-size:30px;">2367</div>
  <div class="t street foot-name" style="left:36px;top:1051px;font-size:23px;">HALVORSEN AVENUE</div>
  <div class="t centre foot-name" style="left:36px;top:1079px;font-size:19px;">MEDICAL CENTRE</div>

  <div class="t address">
    <strong>ADDRESS:</strong>
    2367 Halvorsen Avenue East<br>
    Unit 225<br>
    Scarborough, Ontario<br>
    K7T 2P4
  </div>
</main>
</body>
</html>
```